Event Planning Website

We are interested in redesigning our website. We just launched this company and we offer variety of event planning services. We specialize in wedding planning. We offer all inclusive packages, capturing the proposal, wedding planning, day of directing of the event. We help people save money, stay within budget and do the work so they could enjoy their special occasion.

We are looking to design 5 pages (we are open to suggestions to add or remove/combine), we like social media links (Facebook, instagram, yelp, testimonials) incorporated as recommended: Our existing webpage www.planwithpetal.com, Facebook.com/planwithpetal, http://instagram.com/planwithpetal, http://www.yelp.com/biz/plan-with-petal-san-ramon, logo and flyer are attached. Please let us know if you need additional information. We are looking for a template to be able to easily edit, fill and embed content.

HOME PAGE
This is the landing page, we want it to be informative, attractive, effective leading to contact/lead.

SERVICES
This page should be about our services which we offer (proposal, planning, day of directing), all packages with clean layout detailing the packages.

MEDIA
This page will consist of photo gallery of past events, social media feed, video clips etc.

CONTACT
Modern, hip, minimalistic.

About us
Who we are, the team, bio about each planner within our firm, experience,

Industry/Entity Type

Event Planning

```html
<!DOCTYPE html>
<html lang="en">
<head>
<meta charset="utf-8">
<title>Plan With Petal – Planning &amp; Coordination</title>
<link rel="stylesheet" href="https://fonts.googleapis.com/css2?family=Great+Vibes&family=Lora:ital,wght@0,400;1,400&family=Arimo:wght@400&display=swap">
<style>
  :root {
    --page-bg: #f7f0ea;
    --sheet: #f1e8df;
    --sheet-edge: #e3d2c4;
    --border-soft: #eadbd0;
    --crimson: #c4123a;
    --ink: #222222;
    --body-text: #5a5a5a;
    --rule-dark: #4a4a4a;
    --white: #ffffff;
    --photo-frame: #e6d3c4;
  }
  * { box-sizing: border-box; margin: 0; padding: 0; }
  html, body { width: 1200px; height: 2517px; overflow: hidden; }
  body {
    position: relative;
    background: var(--page-bg);
    font-family: "Arimo", Arial, sans-serif;
    color: var(--body-text);
  }
  .abs { position: absolute; }
  .sheet {
    left: 79px; top: 47px; width: 1042px; height: 2436px;
    background: var(--sheet);
    border: 2px solid var(--sheet-edge);
    box-shadow: 0 0 8px rgba(150,110,90,.25);
  }
  .sheet-inner {
    left: 97px; top: 65px; width: 1006px; height: 2400px;
    border: 2px solid var(--border-soft);
  }
  .corner-ornament { width: 150px; height: 150px; background: radial-gradient(circle at center, rgba(200,160,130,.18), rgba(200,160,130,0) 70%); }

  /* Brand */
  .brand { left: 0; width: 1200px; top: 128px; text-align: center; }
  .brand-row { display: inline-flex; align-items: center; gap: 14px; }
  .brand-mark { width: 40px; height: 40px; border-radius: 50%; border: 2px solid var(--ink); }
  .brand-name { font-family: "Lora", Georgia, serif; font-size: 36px; letter-spacing: 2px; color: var(--ink); line-height: 1; }
  .brand-tag { font-family: "Lora", Georgia, serif; font-size: 11px; letter-spacing: 2px; color: var(--ink); margin-top: 6px; }

  /* Nav */
  .nav { left: 116px; top: 252px; width: 968px; height: 50px; background: var(--white);
    border-top: 3px solid var(--rule-dark); border-bottom: 3px solid var(--rule-dark);
    display: flex; align-items: center; justify-content: space-between; padding: 0 14px; }
  .nav a { font-size: 14px; color: var(--ink); text-decoration: none; letter-spacing: .3px; }
  .nav svg { width: 16px; height: 16px; fill: var(--ink); }

  /* Hero */
  .hero { left: 117px; top: 314px; width: 967px; height: 461px; border: 5px solid var(--white);
    background: linear-gradient(100deg, #7fb3c2 0%, #c8dde3 35%, #eef3f6 60%, #f4f2f8 100%); }
  .hero-title { left: 694px; top: 472px; width: 370px; white-space: nowrap; font-family: "Great Vibes", cursive; font-weight: 400; font-size: 50px; line-height: 1.1; color: var(--crimson); }
  .hero-sub { left: 698px; top: 552px; width: 350px; font-family: "Great Vibes", cursive; font-size: 22px; color: #4a4a4a; line-height: 34px; }
  .hero-dots { left: 1000px; top: 740px; display: flex; gap: 6px; }
  .hero-dots span { width: 13px; height: 13px; border-radius: 50%; border: 2px solid #555; background: #fff; }
  .hero-dots span.active { border-color: var(--crimson); }

  /* Section headings */
  .section-title { left: 0; width: 1200px; text-align: center; font-family: "Great Vibes", cursive; font-weight: 400; font-size: 40px; line-height: 1.2; color: var(--crimson); white-space: nowrap; }
  .divider { left: 0; width: 1200px; display: flex; align-items: center; justify-content: center; gap: 6px; }
  .divider i { display: block; height: 1px; background: var(--crimson); opacity: .6; }
  .divider svg { width: 20px; height: 18px; fill: none; stroke: var(--crimson); stroke-width: 2; }

  /* Intro features */
  .intro-photo { width: 148px; height: 148px; border-radius: 50%; border: 5px solid var(--white); box-shadow: 0 0 4px rgba(0,0,0,.2); }
  .intro-title { font-family: "Lora", Georgia, serif; font-style: italic; font-weight: 400; font-size: 21px; color: #333; white-space: nowrap; }
  .body-copy { font-size: 12px; line-height: 21px; color: var(--body-text); }
  .read-more { font-family: "Great Vibes", cursive; font-size: 18px; color: var(--crimson); text-decoration: none; }

  /* Stages */
  .stage-title { font-family: "Great Vibes", cursive; font-weight: 400; font-size: 26px; line-height: 1.3; color: #333; width: 299px; border-bottom: 3px solid var(--rule-dark); padding-bottom: 2px; }
  .stage-photo { width: 299px; height: 193px; border: 7px solid var(--photo-frame); }

  /* Testimonials */
  .testimonials { left: 116px; top: 1574px; width: 968px; height: 344px; background: var(--white); border: 4px solid #efe6dc; }
  .quote { left: 205px; top: 1694px; width: 790px; text-align: center; font-size: 11.5px; line-height: 23px; color: #666; }
  .quote-mark { font-family: "Lora", Georgia, serif; font-size: 44px; color: #555; line-height: 1; }
  .avatar { left: 549px; top: 1754px; width: 100px; height: 100px; border-radius: 50%; border: 5px solid #f3ece6; box-shadow: 0 0 4px rgba(0,0,0,.2); background: linear-gradient(135deg, #b7c7cf, #e5e0dc); }
  .client-name { left: 0; width: 1200px; top: 1860px; text-align: center; font-family: "Great Vibes", cursive; font-size: 24px; color: var(--crimson); }

  /* Gallery */
  .gallery-photo { top: 2044px; height: 183px; }

  /* Footer */
  .footer-rule { left: 116px; top: 2277px; width: 968px; height: 1px; background: var(--border-soft); }
  .social { left: 0; width: 1200px; top: 2327px; display: flex; justify-content: center; gap: 10px; }
  .social span { width: 32px; height: 32px; border-radius: 50%; border: 2px solid #c9a880; }
  .copyright { left: 0; width: 1200px; top: 2378px; text-align: center; font-size: 11px; color: #444; }
</style>
</head>
<body>
  <div class="abs sheet"></div>
  <div class="abs sheet-inner"></div>
  <div class="abs corner-ornament" style="left:110px;top:78px" role="img" aria-label="Floral flourish ornament"></div>
  <div class="abs corner-ornament" style="left:940px;top:78px" role="img" aria-label="Floral flourish ornament"></div>
  <div class="abs corner-ornament" style="left:110px;top:2300px" role="img" aria-label="Floral flourish ornament"></div>
  <div class="abs corner-ornament" style="left:940px;top:2300px" role="img" aria-label="Floral flourish ornament"></div>

  <header class="abs brand">
    <div class="brand-row"><span class="brand-mark"></span><span class="brand-name">PLAN WITH PETAL</span></div>
    <div class="brand-tag">PLANNING &amp; COORDINATION</div>
  </header>

  <nav class="abs nav">
    <svg viewBox="0 0 20 18"><path d="M10 17 1.5 8.5A4.8 4.8 0 0 1 10 3a4.8 4.8 0 0 1 8.5 5.5Z"/></svg>
    <a href="#">HOME</a><a href="#">SERVICES</a><a href="#">MEDIA</a><a href="#">PACKAGES</a><a href="#">CONTACT</a><a href="#">ABOUT US</a>
    <svg viewBox="0 0 20 18"><path d="M10 17 1.5 8.5A4.8 4.8 0 0 1 10 3a4.8 4.8 0 0 1 8.5 5.5Z"/></svg>
  </nav>

  <section>
    <div class="abs hero" role="img" aria-label="Smiling bride and groom with a white bouquet by the water"></div>
    <h1 class="abs hero-title">Plan With Petal</h1>
    <p class="abs hero-sub">It is a long established fact that a reader will a page when looking at its layout.</p>
    <div class="abs hero-dots"><span></span><span class="active"></span><span></span><span></span></div>
  </section>

  <h2 class="abs section-title" style="top:814px">Welcome To Plan With Petal</h2>
  <div class="abs divider" style="top:874px"><i style="width:230px"></i><svg viewBox="0 0 20 18"><path d="M10 16 2 8.5A4.5 4.5 0 0 1 10 3a4.5 4.5 0 0 1 8 5.5Z"/></svg><i style="width:230px"></i></div>

  <div class="abs intro-photo" style="left:117px;top:919px;background:linear-gradient(135deg,#7fb0cf,#d9c6b5)" role="img" aria-label="Couple kissing outdoors"></div>
  <h3 class="abs intro-title" style="left:287px;top:924px">Contrary to popular belief</h3>
  <p class="abs body-copy" style="left:289px;top:960px;width:295px">It is a long established fact that a reader will be dis-tracted by the readable content of a page when looking at its layout. The point of using Lorem web sites still in their infancy..</p>
  <a class="abs read-more" href="#" style="left:289px;top:1052px">Read More</a>

  <div class="abs intro-photo" style="left:624px;top:919px;background:linear-gradient(135deg,#3f5a4a,#e8e2dc)" role="img" aria-label="Bride and groom embracing"></div>
  <h3 class="abs intro-title" style="left:793px;top:924px">Contrary to popular belief</h3>
  <p class="abs body-copy" style="left:795px;top:960px;width:295px">It is a long established fact that a reader will be dis-tracted by the readable content of a page when looking at its layout. The point of using Lorem web sites still in their infancy..</p>
  <a class="abs read-more" href="#" style="left:795px;top:1052px">Read More</a>

  <h3 class="abs stage-title" style="left:116px;top:1144px">The Proposal</h3>
  <div class="abs stage-photo" style="left:116px;top:1208px;background:linear-gradient(135deg,#3a2a25,#8e1a25 50%,#4b3a30)" role="img" aria-label="Red roses centrepiece on a candlelit table"></div>
  <p class="abs body-copy" style="left:116px;top:1416px;width:299px">It is a long established fact that a reader will be distracted by the readable content of a page when looking at its layout. The point of using Lorem web sites still in their infancy..</p>
  <a class="abs read-more" href="#" style="left:116px;top:1508px">Read More</a>

  <h3 class="abs stage-title" style="left:450px;top:1144px">The Planning</h3>
  <div class="abs stage-photo" style="left:450px;top:1208px;background:linear-gradient(135deg,#8a3e52,#8ea09a 50%,#6f5a4e)" role="img" aria-label="Draped ceremony arch with white chairs in a garden"></div>
  <p class="abs body-copy" style="left:450px;top:1416px;width:299px">It is a long established fact that a reader will be distracted by the readable content of a page when looking at its layout. The point of using Lorem web sites still in their infancy..</p>
  <a class="abs read-more" href="#" style="left:450px;top:1508px">Read More</a>

  <h3 class="abs stage-title" style="left:784px;top:1144px">The Day</h3>
  <div class="abs stage-photo" style="left:784px;top:1208px;background:linear-gradient(135deg,#c9874a,#e8e3de 50%,#b07440)" role="img" aria-label="Couple at the altar under golden drapes"></div>
  <p class="abs body-copy" style="left:784px;top:1416px;width:299px">It is a long established fact that a reader will be distracted by the readable content of a page when looking at its layout. The point of using Lorem web sites still in their infancy..</p>
  <a class="abs read-more" href="#" style="left:784px;top:1508px">Read More</a>

  <section>
    <div class="abs testimonials"></div>
    <h2 class="abs section-title" style="top:1608px;font-size:34px">Our Testimonials</h2>
    <div class="abs divider" style="top:1658px"><i style="width:130px"></i><svg viewBox="0 0 20 18"><path d="M10 16 2 8.5A4.5 4.5 0 0 1 10 3a4.5 4.5 0 0 1 8 5.5Z"/></svg><i style="width:130px"></i></div>
    <span class="abs quote-mark" style="left:172px;top:1680px">&ldquo;</span>
    <p class="abs quote">Our wedding was enchanting from beginning to end and having Lorena as our coordinator was the icing on the cake! She took a heavy load of stress off producer, and the editor all at once! We were just actors playing the part in a well detailed and orchestrated movie!</p>
    <span class="abs quote-mark" style="left:906px;top:1742px">&rdquo;</span>
    <div class="abs avatar" role="img" aria-label="Portrait of the couple"></div>
    <p class="abs client-name">Tom &amp; Clara</p>
  </section>

  <h2 class="abs section-title" style="top:1948px;font-size:36px">Latest Gallery</h2>
  <div class="abs divider" style="top:1998px"><i style="width:130px"></i><svg viewBox="0 0 20 18"><path d="M10 16 2 8.5A4.5 4.5 0 0 1 10 3a4.5 4.5 0 0 1 8 5.5Z"/></svg><i style="width:130px"></i></div>
  <div class="abs gallery-photo" style="left:116px;width:231px;background:linear-gradient(135deg,#4f6a4a,#f3f1ee 55%,#5c7a52)" role="img" aria-label="Bride in a ruffled gown on a green sofa"></div>
  <div class="abs gallery-photo" style="left:364px;width:232px;background:linear-gradient(135deg,#5a4a40,#9a1f2e 50%,#8a9a92)" role="img" aria-label="Reception table with red flowers and candles"></div>
  <div class="abs gallery-photo" style="left:609px;width:230px;background:linear-gradient(135deg,#d8dde0,#4a4a4e 50%,#e9e6e2)" role="img" aria-label="Couple kissing holding chalkboard signs"></div>
  <div class="abs gallery-photo" style="left:854px;width:230px;background:linear-gradient(135deg,#b27a4a,#e3b487 50%,#9a6438)" role="img" aria-label="Stack of decorated wedding cookies"></div>

  <footer>
    <div class="abs footer-rule"></div>
    <div class="abs social"><span></span><span></span><span></span><span></span><span></span></div>
    <p class="abs copyright">&copy; Copy Rights Plan With Petal 2105 All copyrights Reserved.</p>
  </footer>
</body>
</html>
```